Quorvan Medical business cards

Double sided business cards.

Medical technology consulting company.

Business cards with two names on the front, upper to middle left:

Dr Colin R. Harbury BMed GAICD +61412558907
Dr Owen Palatsky PhD MCommrclLaw +61437619042

Email and website addresses bottom right:

colin@quorvanmedical.com.au
www.quorvanmedical.com.au

Tree logo (as per attached file) on front in a suitable position.

Tag line (as per attached files) on the back.

Need a file format to upload to Paper Haven or Cardlyner.

```html
<!DOCTYPE html>
<html lang="en">
<head>
<meta charset="utf-8">
<title>Quorvan Medical business cards</title>
<link rel="stylesheet" href="https://fonts.googleapis.com/css2?family=Open+Sans:wght@400;600&family=Roboto+Condensed:wght@700&display=swap">
<style>
  :root {
    --backdrop: #222222;
    --paper: #ffffff;
    --leaf-green: #4e9140;
    --deep-maroon: #5a0f12;
    --card-w: 540px;
    --card-h: 300px;
  }
  * { box-sizing: border-box; margin: 0; padding: 0; }
  html, body { width: 1200px; height: 711px; overflow: hidden; background: var(--backdrop); }
  .stage { position: relative; width: 1200px; height: 711px; }
  .card {
    position: absolute; top: 205px;
    width: var(--card-w); height: var(--card-h);
    background: var(--paper); overflow: hidden;
    box-shadow: 0 10px 28px rgba(0,0,0,.55);
  }
  .card--back { left: 40px; }
  .card--front { left: 620px; }
  .card-bands { position: absolute; inset: 0; width: 100%; height: 100%; }

  .brand { display: flex; align-items: center; gap: 10px; font-family: "Open Sans", sans-serif; font-weight: 400; color: var(--deep-maroon); letter-spacing: 1px; white-space: nowrap; }
  .brand-dot { border-radius: 50%; background: var(--leaf-green); flex: none; }

  .card--back .brand { position: absolute; left: 0; right: 0; top: 100px; justify-content: center; font-size: 38px; }
  .card--back .brand-dot { width: 32px; height: 32px; }
  .tagline { position: absolute; left: 0; right: 0; top: 172px; text-align: center; font-family: "Open Sans", sans-serif; font-size: 21px; color: var(--leaf-green); letter-spacing: .5px; white-space: nowrap; }
  .tagline .sep { color: var(--deep-maroon); margin: 0 8px; }

  .card--front .brand { position: absolute; right: 26px; top: 74px; font-size: 24px; }
  .card--front .brand-dot { width: 22px; height: 22px; }

  .partners { position: absolute; left: 28px; top: 40px; font-family: "Roboto Condensed", sans-serif; }
  .partner { margin-bottom: 14px; }
  .partner:nth-child(2) { margin-left: 44px; }
  .partner-name { color: var(--leaf-green); font-weight: 700; font-size: 22px; line-height: 1.1; white-space: nowrap; }
  .partner-phone { display: flex; align-items: center; gap: 6px; margin-top: 3px; font-family: "Open Sans", sans-serif; font-size: 15px; color: var(--deep-maroon); }

  .contact { position: absolute; right: 22px; bottom: 54px; text-align: right; font-family: "Open Sans", sans-serif; font-size: 13px; color: var(--deep-maroon); line-height: 1.55; }
  .contact-row { display: flex; justify-content: flex-end; align-items: center; gap: 6px; }
  .contact-icon { width: 11px; height: 11px; border-radius: 50%; background: var(--leaf-green); }
</style>
</head>
<body>
<main class="stage">

  <section class="card card--back" aria-label="Card back">
    <svg class="card-bands" viewBox="0 0 540 300" aria-hidden="true">
      <polygon points="0,282 150,246 168,256 420,256 438,246 540,224 540,300 0,300" fill="var(--leaf-green)"/>
      <polygon points="150,246 172,262 420,262 438,246 430,236 160,236" fill="var(--paper)"/>
      <polygon points="168,246 178,270 418,270 428,246" fill="var(--deep-maroon)"/>
    </svg>
    <div class="brand"><span class="brand-dot"></span>QUORVAN MEDICAL</div>
    <p class="tagline">Idea<span class="sep">|</span>Development<span class="sep">|</span>Market</p>
  </section>

  <section class="card card--front" aria-label="Card front">
    <svg class="card-bands" viewBox="0 0 540 300" aria-hidden="true">
      <polygon points="0,0 248,0 238,20 0,20" fill="var(--leaf-green)"/>
      <polygon points="350,300 358,252 540,252 540,300" fill="var(--deep-maroon)"/>
    </svg>
    <div class="brand"><span class="brand-dot"></span>QUORVAN MEDICAL</div>

    <div class="partners">
      <div class="partner">
        <p class="partner-name">Dr Colin R. Harbury<br>BMed GAICD</p>
        <p class="partner-phone">
          <svg width="12" height="12" viewBox="0 0 24 24" aria-hidden="true"><path fill="var(--deep-maroon)" d="M6.6 10.8a15 15 0 0 0 6.6 6.6l2.2-2.2a1 1 0 0 1 1-.25 11.4 11.4 0 0 0 3.6.57 1 1 0 0 1 1 1V20a1 1 0 0 1-1 1A17 17 0 0 1 3 4a1 1 0 0 1 1-1h3.5a1 1 0 0 1 1 1c0 1.25.2 2.45.57 3.57a1 1 0 0 1-.25 1z"/></svg>
          +61412558907
        </p>
      </div>
      <div class="partner">
        <p class="partner-name">Dr Owen Palatsky<br>PhD MCommrclLaw</p>
        <p class="partner-phone">
          <svg width="12" height="12" viewBox="0 0 24 24" aria-hidden="true"><path fill="var(--deep-maroon)" d="M6.6 10.8a15 15 0 0 0 6.6 6.6l2.2-2.2a1 1 0 0 1 1-.25 11.4 11.4 0 0 0 3.6.57 1 1 0 0 1 1 1V20a1 1 0 0 1-1 1A17 17 0 0 1 3 4a1 1 0 0 1 1-1h3.5a1 1 0 0 1 1 1c0 1.25.2 2.45.57 3.57a1 1 0 0 1-.25 1z"/></svg>
          +61437619042
        </p>
      </div>
    </div>

    <div class="contact">
      <p class="contact-row">colin@quorvanmedical.com.au <span class="contact-icon"></span></p>
      <p class="contact-row">www.quorvanmedical.com.au <span class="contact-icon"></span></p>
    </div>
  </section>

</main>
</body>
</html>
```